Wine Label for New exciting wine company

We require a label thats quirky and stands out in the crowded shelves of liquor stores. We are happy to use such colours as burnt orange, reds etc, or we are opened to any new brave designs with designers choice of colours. Label not to be to busy, but must have a presence. Label size to be approx 9cm Width and 10cm Long.
By the way the name of the wine ladel is Tallowbark Wines. The word Wines does not need to show on the label

Thanks
Rod Pettiford

Hi Everyone, we had a label we started a few years back called Hammockbay Wines which was a very successful wine and is still being sold today. It was fun and funky and stood out on the shelf, and thats the sort of label we wanted designed. It can be along different lines but the concept is what we are looking at.
Please go to their site www.hammockbaywines.com.au and have a look at the label.
Saying that a couple of the sesigns that have come through have merit and will still be considered.
Thanks fot all your designs so far
Rod Pettiford

```html
<!DOCTYPE html>
<html lang="en">
<head>
<meta charset="utf-8">
<title>Tallowbark – Cabernet Merlot label</title>
<link rel="stylesheet" href="https://fonts.googleapis.com/css2?family=Questrial&family=Roboto+Condensed:wght@400&family=Pinyon+Script&display=swap">
<style>
  :root {
    --backdrop: #6e6c73;
    --label-black: #0c0c0c;
    --label-white: #fbfbfa;
    --accent-orange: #ee9a1c;
    --vintage-grey: #8a8a8a;
    --script-grey: #5a5a5a;
    --wines-grey: #9a9a9a;
    --glass-beige-light: #e4e0c8;
    --glass-beige-dark: #b9b393;
    --wine-red: #9c0d10;
    --mark-dark: #1f1a15;
  }
  * { margin: 0; padding: 0; box-sizing: border-box; }
  html, body {
    width: 1200px;
    height: 1070px;
    overflow: hidden;
    background: var(--backdrop);
  }
  .label {
    position: absolute;
    left: 60px;
    top: 175px;
    width: 1080px;
    height: 720px;
    display: flex;
    box-shadow: 0 12px 40px rgba(0,0,0,0.35);
  }
  /* Black brand panel */
  .brand-panel {
    position: relative;
    width: 300px;
    height: 100%;
    background: var(--label-black);
    overflow: hidden;
  }
  /* Horizontal stack turned to read bottom-to-top */
  .brand-stack {
    position: absolute;
    left: -210px;
    top: 210px;
    width: 720px;
    height: 300px;
    transform: rotate(-90deg);
  }
  .brand-name {
    position: absolute;
    left: 22px;
    bottom: 28px;
    font-family: "Questrial", sans-serif;
    font-size: 134px;
    line-height: 1;
    color: var(--accent-orange);
    white-space: nowrap;
    letter-spacing: -2px;
  }
  .brand-wines {
    position: absolute;
    right: 20px;
    bottom: 4px;
    font-family: "Questrial", sans-serif;
    font-size: 24px;
    line-height: 1;
    color: var(--wines-grey);
    letter-spacing: 1px;
  }
  .region {
    position: absolute;
    left: 150px;
    bottom: 150px;
    font-family: "Pinyon Script", cursive;
    font-size: 38px;
    line-height: 1;
    color: var(--script-grey);
    white-space: nowrap;
  }
  /* White varietal panel */
  .varietal-panel {
    position: relative;
    width: 400px;
    height: 100%;
    background: var(--label-white);
  }
  .vintage {
    position: absolute;
    left: 26px;
    top: 26px;
    font-family: "Roboto Condensed", sans-serif;
    font-size: 46px;
    color: var(--vintage-grey);
    line-height: 1;
  }
  .varietal {
    position: absolute;
    left: 26px;
    top: 74px;
    font-family: "Roboto Condensed", sans-serif;
    font-size: 44px;
    color: var(--accent-orange);
    line-height: 1;
    letter-spacing: -0.5px;
  }
  .sofa-photo {
    position: absolute;
    left: 0;
    top: 300px;
    width: 400px;
    height: 300px;
    background: radial-gradient(ellipse at 45% 50%, #f6b21e 0%, #e89a10 45%, rgba(238,154,28,0.15) 72%, rgba(251,251,250,0) 80%);
  }
  /* Glass photo panel */
  .glass-panel {
    position: relative;
    flex: 1;
    height: 100%;
    overflow: hidden;
  }
  .glass-photo {
    position: absolute;
    inset: 0;
    background:
      linear-gradient(180deg, rgba(0,0,0,0) 0%, rgba(0,0,0,0) 52%, var(--wine-red) 56%, #6e0608 100%) 120px 0 / 260px 100% no-repeat,
      linear-gradient(90deg, var(--glass-beige-light) 0%, var(--glass-beige-dark) 100%);
  }
  .glass-mark {
    position: absolute;
    right: 34px;
    top: 60px;
    display: flex;
    align-items: center;
    gap: 10px;
    font-family: "Questrial", sans-serif;
    font-size: 30px;
    color: var(--mark-dark);
  }
  .glass-mark svg { display: block; }
</style>
</head>
<body>
  <main class="label">
    <section class="brand-panel">
      <div class="brand-stack">
        <span class="region">Jarrah Creek</span>
        <span class="brand-name">Tallowbark</span>
        <span class="brand-wines">wines</span>
      </div>
    </section>

    <section class="varietal-panel">
      <p class="vintage">2007</p>
      <p class="varietal">Cabernet Merlot</p>
      <div class="sofa-photo" role="img" aria-label="Photograph of a curvy orange leather sofa on a white floor"></div>
    </section>

    <section class="glass-panel">
      <div class="glass-photo" role="img" aria-label="Close-up photograph of a wine glass filled with red wine against a beige background"></div>
      <div class="glass-mark">
        <svg width="26" height="26" viewBox="0 0 26 26" aria-hidden="true"><circle cx="13" cy="13" r="12" fill="var(--mark-dark)"/></svg>
        <span>Tallowbark</span>
      </div>
    </section>
  </main>
</body>
</html>
```